IT Consulting Business Card Design

We need a business card on our company name....which is a IT consulting and staffing company. We also train masters graduates in various IT courses. 70% of the time these cards will be handed out to the graduate students at the universities. 30% for our clients and business partners. We are uploading our company logo...would like to see something that matches our logo or blends with it. Please visit www.brightvaleworks.com for more details on logo and colors.

Target Market(s)

70% of the time these cards will be handed out to the graduate students at the universities. 30% for our clients and business partners.

Industry/Entity Type

Business

Contact Information for Business Card

Ravi Kondamuri
Vice-President
Bright Vale Works Inc
3807 Morrow Lane, Suite 412
East Brookridge, NJ 07315
ravi@brightvaleworks.com
Office : 1-866-219-3840 X 515
Cell number : 732-581-9034

Requirements
Nice to have
• may be company logo and name on the back of the card and detials on the other side...just a thought..!!

```html
<!DOCTYPE html>
<html lang="en">
<head>
<meta charset="utf-8">
<title>Bright Vale Works – Business Card</title>
<link href="https://fonts.googleapis.com/css2?family=PT+Sans:wght@400;700&display=swap" rel="stylesheet">
<style>
  :root {
    --bg: #e6e7e8;
    --card: #ffffff;
    --red: #e31e26;
    --ink: #3a3a3c;
    --shadow: rgba(0, 0, 0, 0.18);
  }
  * { margin: 0; padding: 0; box-sizing: border-box; }
  html, body {
    width: 1200px; height: 900px; overflow: hidden;
    background: var(--bg);
    font-family: "PT Sans", "Helvetica Neue", Arial, sans-serif;
  }
  .canvas { position: relative; width: 1200px; height: 900px; }
  .card {
    position: absolute;
    width: 560px; height: 320px;
    background: var(--card);
    box-shadow: 0 10px 28px var(--shadow);
    overflow: hidden;
  }
  .card--front { left: 90px; top: 100px; }
  .card--back { left: 550px; top: 480px; }

  .brand { display: flex; align-items: center; gap: 12px; }
  .brand__dot { flex: none; display: block; }
  .brand__name {
    font-weight: 700; color: var(--ink);
    letter-spacing: 0.3px; white-space: nowrap; line-height: 1;
  }

  .card--front .brand {
    position: absolute; right: 64px; top: 176px;
  }
  .card--front .brand__name { font-size: 34px; }

  .card--back .brand {
    position: absolute; right: 34px; top: 28px;
  }
  .card--back .brand__name { font-size: 28px; }

  .contact {
    position: absolute; right: 34px; top: 84px;
    text-align: right; line-height: 1.2;
  }
  .contact__name { color: var(--red); font-size: 18px; }
  .contact__role { color: var(--ink); font-size: 15px; margin-bottom: 8px; }
  .contact__address, .contact__reach { color: var(--red); font-size: 11px; font-style: normal; }
  .contact__address { margin-bottom: 10px; }
  .contact__web { color: var(--ink); font-size: 11px; margin-top: 6px; }

  .card__band {
    position: absolute; left: 0; right: 0; bottom: 0;
    height: 30px; background: var(--red);
  }
</style>
</head>
<body>
<main class="canvas">

  <section class="card card--front" aria-label="Business card, front">
    <div class="brand">
      <svg class="brand__dot" width="32" height="32" viewBox="0 0 32 32" aria-hidden="true">
        <circle cx="16" cy="16" r="16" fill="var(--red)"/>
      </svg>
      <span class="brand__name">BRIGHT VALE WORKS</span>
    </div>
  </section>

  <section class="card card--back" aria-label="Business card, back">
    <div class="brand">
      <svg class="brand__dot" width="26" height="26" viewBox="0 0 26 26" aria-hidden="true">
        <circle cx="13" cy="13" r="13" fill="var(--red)"/>
      </svg>
      <span class="brand__name">BRIGHT VALE WORKS</span>
    </div>

    <div class="contact">
      <p class="contact__name">Ravi Kondamuri</p>
      <p class="contact__role">Vice-President Bright Vale Works Inc</p>
      <address class="contact__address">
        3807 Morrow Lane, Suite 412<br>
        East Brookridge, NJ 07315
      </address>
      <p class="contact__reach">
        ravi@brightvaleworks.com<br>
        Office : 1-866-219-3840 X 515<br>
        Cell number : 732-581-9034
      </p>
      <p class="contact__web">www.brightvaleworks.com</p>
    </div>

    <div class="card__band"></div>
  </section>

</main>
</body>
</html>
```